School Learner profile graphic representation

I have a set of ideas around communicating our school 'learner profile'. These represent the attitudes, habits and dispositions we are trying to develop through our curriculum and wider enrichment programme. I want the links between the ideas and concepts to be represented in some form of an inforgraphic which can be published and displayed for the whole community to connect with. we run two schools and want the profile to represent for both.

Target Market(s)

Students, Parents, Teachers, Wider community in education

Industry/Entity Type

Education

Font styles to use
Other font styles liked:
• Johnson p22

Colors

Designer to choose colors to be used in the design.

Requirements
Must have
• See my diagram in the ppt.
• The statements Aspiration, Agency, Agility, Altitude with the supporting descriptions. Ideally the values in the center is also represented. The two school logos should also be present somehow (both emblems at least). Let me know if the full logo files are required
Nice to have
• the numbering shown in my diagram is not absolutely necessary is it is not necessarily a linear process and rather cyclical and cross reinforcing

```html
<!DOCTYPE html>
<html lang="en">
<head>
<meta charset="utf-8">
<title>Envisioning Our Learners</title>
<link rel="stylesheet" href="https://fonts.googleapis.com/css2?family=Montserrat:wght@400;600;700;800&family=Roboto+Condensed:wght@400;700&family=Poppins:wght@300;700&display=swap">
<style>
  :root {
    --red: #BB1F2A;
    --red-bright: #E5252C;
    --teal: #175C55;
    --ink: #1E1E1E;
    --white: #FFFFFF;
    --paper-light: #FBFBFB;
    --paper-dark: #ECECEC;
    --core: #E8E8E8;
    --rock: #4A4A4A;
    --rock-light: #8A8A8A;
  }
  * { margin: 0; padding: 0; box-sizing: border-box; }
  html, body { width: 1200px; height: 889px; overflow: hidden; background: var(--white); }
  .poster { position: relative; width: 1200px; height: 889px; overflow: hidden; background: var(--white); font-family: "Roboto Condensed", sans-serif; }

  .header { position: absolute; left: 0; top: 0; width: 1200px; height: 181px; background: var(--white); }
  .brand { position: absolute; display: flex; align-items: center; }
  .brand-dot { width: 116px; height: 116px; border-radius: 50%; background: var(--red-bright); flex: none; }
  .brand--private { left: 90px; top: 27px; }
  .brand--private .brand-text { margin-left: 17px; }
  .brand--private .brand-name { font-family: "Montserrat", sans-serif; font-weight: 800; font-size: 20.3px; color: #111; letter-spacing: -0.6px; line-height: 1.1; white-space: nowrap; }
  .brand--private .brand-tagline { font-family: "Poppins", sans-serif; font-weight: 300; font-size: 15.5px; color: #222; letter-spacing: 2.4px; margin-top: 4px; white-space: nowrap; }
  .brand--community { left: 730px; top: 27px; }
  .brand--community .brand-dot { background: var(--red); }
  .brand--community .brand-text { margin-left: 14px; font-family: "Montserrat", sans-serif; font-weight: 600; color: var(--red); line-height: 1.2; white-space: nowrap; }
  .brand--community .line-1 { font-size: 24px; letter-spacing: 3.5px; }
  .brand--community .line-2, .brand--community .line-3 { font-size: 19px; letter-spacing: 5px; }

  .divider-wedge { position: absolute; left: 0; top: 0; }

  .title-band { position: absolute; left: 0; top: 181px; width: 1200px; height: 78px; background: var(--red); }
  .title-band h1 { position: absolute; left: 0; right: 0; top: 12px; text-align: center; font-family: "Montserrat", sans-serif; font-weight: 700; font-size: 48px; letter-spacing: 7.8px; color: var(--white); line-height: 54px; white-space: nowrap; }
  .title-rule { position: absolute; width: 88px; height: 4px; background: var(--white); }

  .content { position: absolute; left: 0; top: 259px; width: 1200px; height: 567px; background: radial-gradient(ellipse at 45% 50%, var(--paper-light) 0%, var(--paper-dark) 100%); }
  .diagram { position: absolute; left: 0; top: 0; width: 1200px; height: 889px; }

  .ring-label { position: absolute; font-family: "Montserrat", sans-serif; font-weight: 700; font-size: 18px; color: var(--white); line-height: 23px; }
  .core-text { position: absolute; left: 182px; top: 488px; width: 200px; text-align: center; font-weight: 700; font-size: 27px; line-height: 32.5px; color: #111; }

  .trait { position: absolute; left: 588px; }
  .trait h2 { font-weight: 400; font-size: 35px; line-height: 40px; color: var(--teal); letter-spacing: -0.2px; white-space: nowrap; }
  .trait h2 strong { font-weight: 700; }
  .trait p { font-size: 22px; line-height: 26px; color: var(--ink); margin-top: 5px; white-space: nowrap; }

  .climber-art { position: absolute; left: 1023px; top: 688px; width: 129px; height: 60px; border-radius: 4px; background: linear-gradient(160deg, var(--rock-light), var(--rock)); }

  .footnote { position: absolute; left: 0; top: 826px; width: 1200px; height: 63px; background: var(--red); color: var(--white); font-size: 26.4px; line-height: 63px; text-align: center; white-space: nowrap; }
</style>
</head>
<body>
<div class="poster">
  <header class="header">
    <div class="brand brand--private">
      <span class="brand-dot"></span>
      <div class="brand-text">
        <div class="brand-name">Cedar Grove Private School</div>
        <div class="brand-tagline">Where every child is special</div>
      </div>
    </div>
    <div class="brand brand--community">
      <span class="brand-dot"></span>
      <div class="brand-text">
        <div class="line-1">CEDAR GROVE</div>
        <div class="line-2">COMMUNITY</div>
        <div class="line-3">SCHOOL</div>
      </div>
    </div>
  </header>

  <div class="title-band">
    <span class="title-rule" style="left:0;top:29px"></span>
    <span class="title-rule" style="left:0;top:45px"></span>
    <span class="title-rule" style="right:0;top:29px"></span>
    <span class="title-rule" style="right:0;top:45px"></span>
    <h1>ENVISIONING OUR LEARNERS</h1>
  </div>

  <svg class="divider-wedge" width="1200" height="183" viewBox="0 0 1200 183" aria-hidden="true">
    <polygon points="561,0 638,0 600,183" fill="var(--red)"/>
  </svg>

  <section class="content"></section>

  <svg class="diagram" viewBox="63 83 2105 1487" preserveAspectRatio="none" aria-hidden="true">
    <g fill="none" stroke="var(--teal)" stroke-width="5">
      <polyline points="335,720 335,601 1040,601"/>
      <polyline points="885,835 1040,835"/>
      <polyline points="855,1260 970,1260 970,1072 1040,1072"/>
    </g>
    <g fill="var(--teal)">
      <polygon points="1032,585 1062,601 1032,617 1040,601"/>
      <polygon points="1032,819 1062,835 1032,851 1040,835"/>
      <polygon points="1032,1056 1062,1072 1032,1088 1040,1072"/>
      <polygon points="1032,1294 1062,1310 1032,1326 1040,1310"/>
    </g>
    <circle cx="558" cy="1025" r="379" fill="var(--teal)"/>
    <circle cx="558" cy="1025" r="224" fill="var(--white)"/>
    <circle cx="558" cy="1025" r="195" fill="var(--core)"/>
    <g fill="none" stroke="var(--white)" stroke-width="7" stroke-linejoin="miter">
      <polyline points="535,627 437,732 522,806"/>
      <polyline points="765,1103 860,1050 918,1150"/>
      <polyline points="358,1132 358,1243 243,1243"/>
    </g>
  </svg>

  <div class="ring-label" style="left:400px;top:452px">Mind</div>
  <div class="ring-label" style="left:85px;top:481px">Attitude<br>and<br>Spirit</div>
  <div class="ring-label" style="left:270px;top:724px">Heart</div>
  <div class="core-text">* VALUES<br>MORALS<br>PRINCIPLES<br>ETHICS</div>

  <div class="trait" style="top:276px">
    <h2>Learners with <strong>Agility</strong></h2>
    <p>Are determined, equipped and able to accomplish great things.</p>
  </div>
  <div class="trait" style="top:411px">
    <h2>Learners with <strong>Agency</strong></h2>
    <p>Believe in their capacity and responsibility to do great things.</p>
  </div>
  <div class="trait" style="top:545px">
    <h2>Learners with <strong>Aspiration</strong></h2>
    <p>Inspired and Believe in pursuing great things</p>
  </div>
  <div class="trait" style="top:679px">
    <h2>Learners with <strong>Altitude</strong></h2>
    <p>Achieve great things and work to elevate others.</p>
  </div>

  <div class="climber-art" role="img" aria-label="Illustration of a climber ascending a mountain peak"></div>

  <footer class="footnote">* VALUES MORALS PRINCIPLES ETHICS : This represents the metaphorical compass for the&nbsp; descriptors 1 - 4</footer>
</div>
</body>
</html>
```